Hochwertiges Etiketten-Design für edle Destillate
Zielgruppe
Wir sind ein Familiengeführter Brennereibetrieb wo wir edle Destillate (Obstbrände und Liköre) herstellen.
Aufgabenstellung
Wir suchen ein hochwertiges Etikett welches eine sofortige Wiedererkennung hat. Unser jetziges Etikett soll als Vorlage gelten, jedoch einiges aufgewertet werden. Unser Logo und und die Farbe Rot soll auf jeden Fall darin vorkommen.
Dies sind unsere verwendeten Flaschen
https://www.vandoro.com/kelm-flasche-500ml-weissglas-mdg.-gpi-28-karton-50stk.html?cPath=5_6
https://www.vandoro.com/kelm-flasche-200ml-weissglas-mdg.-gpi-28-karton-45stk.html?cPath=5_6
https://www.vandoro.com/urma-500-ml-weissglas-mdg.-gpi-28-karton-46stk.html?cPath=5_6
https://www.vandoro.com/urma-200ml-weissglas-mdg.-gpi-28-karton-90stk.html?cPath=5_6
das Design soll skalierbar und auf andere Größen anwendbar sein
Folgende Angaben müssen auf dem Etikett sein (austauschbar):
-Sorte: z.B. Williams
-Produkt: zB. Birnenbrand
-Losnummer: z.B. K3F57382
-Inhalt: z.B. 500ml
-Alkoholgehalt: 40% vol
-Adresse

```html
<!DOCTYPE html>
<html lang="de">
<head>
<meta charset="utf-8">
<title>Hallmeier Edelbrände – Williams Birnenbrand Etiketten</title>
<link href="https://fonts.googleapis.com/css2?family=Mrs+Saint+Delafield&family=Oswald:wght@400;500&family=Pathway+Gothic+One&family=Libre+Baskerville&display=swap" rel="stylesheet">
<style>
  :root {
    --page: #ffffff;
    --slate-light: #2c3038;
    --slate-mid: #17191d;
    --slate-dark: #050506;
    --brand-red: #e30613;
    --ornament-red: #a3141c;
    --ink: #ffffff;
    --rule: rgba(255,255,255,0.85);
  }
  * { box-sizing: border-box; margin: 0; padding: 0; }
  html, body { width: 698px; height: 1200px; overflow: hidden; background: var(--page); }
  .sheet { position: relative; width: 698px; height: 1200px; }

  .label {
    position: absolute;
    color: var(--ink);
    background: radial-gradient(ellipse 75% 45% at 50% 42%, var(--slate-light) 0%, var(--slate-mid) 55%, var(--slate-dark) 100%);
    overflow: hidden;
  }
  .label--tall { left: 35px; top: 393px; width: 209px; height: 413px; }
  .label--wide { left: 372px; top: 429px; width: 290px; height: 338px; }

  .house-name, .house-line {
    position: absolute; left: 0; right: 0; text-align: center;
    font-family: "Libre Baskerville", serif; letter-spacing: 0.08em; line-height: 1;
  }
  .house-rule {
    position: absolute; height: 1px; background: var(--brand-red);
  }
  .label--tall .house-name { top: 30px; font-size: 8px; }
  .label--tall .house-rule { left: 84px; width: 41px; top: 47px; }
  .label--tall .house-line { top: 56px; font-size: 10px; }
  .label--wide .house-name { top: 22px; font-size: 6.5px; }
  .label--wide .house-rule { left: 128px; width: 34px; top: 35px; }
  .label--wide .house-line { top: 42px; font-size: 7.5px; }

  .variety {
    position: absolute; left: 0; right: 0; text-align: center;
    font-family: "Mrs Saint Delafield", cursive; font-weight: 400; line-height: 1;
  }
  .label--tall .variety { top: 92px; font-size: 72px; }
  .label--wide .variety { top: 70px; font-size: 84px; }

  .product {
    position: absolute; left: 0; right: 0; text-align: center;
    font-family: "Oswald", sans-serif; font-weight: 500; line-height: 1.15;
  }
  .label--tall .product { top: 182px; font-size: 10px; letter-spacing: 7px; padding-left: 7px; }
  .label--wide .product { top: 168px; font-size: 10px; letter-spacing: 9px; padding-left: 9px; }

  .ornament {
    position: absolute; width: 18px; height: 6px; border-radius: 3px;
    background: linear-gradient(90deg, transparent, var(--ornament-red), transparent);
  }
  .label--tall .ornament--left { left: 37px; top: 192px; }
  .label--tall .ornament--right { left: 154px; top: 192px; }
  .label--wide .ornament--left { left: 45px; top: 174px; }
  .label--wide .ornament--right { left: 227px; top: 174px; }

  .facts { position: absolute; border: 0.8px solid var(--rule); }
  .facts .cell {
    position: absolute; border: 0.8px solid var(--rule);
    display: flex; align-items: center; justify-content: center; text-align: center;
  }
  .spec { font-family: "Oswald", sans-serif; font-weight: 500; letter-spacing: 0.06em; white-space: nowrap; }
  .estimated { font-family: "Libre Baskerville", serif; font-size: 1.1em; margin-left: 3px; }
  .maker, .lot { font-family: "Pathway Gothic One", sans-serif; line-height: 1.3; white-space: nowrap; }

  .mark { display: flex; align-items: center; gap: 4px; font-family: "Oswald", sans-serif; font-weight: 500; }
  .mark-dot { border-radius: 50%; background: var(--brand-red); }

  .label--tall .facts { left: 18px; top: 250px; width: 176px; height: 144px; }
  .label--tall .logo-cell { left: 0; top: 0; width: 77px; height: 90px; }
  .label--tall .volume-cell { left: 77px; top: 0; width: 99px; height: 44px; }
  .label--tall .abv-cell { left: 77px; top: 44px; width: 99px; height: 46px; }
  .label--tall .maker-cell { left: 0; top: 90px; width: 176px; height: 36px; }
  .label--tall .lot-cell { left: 0; top: 126px; width: 176px; height: 18px; }
  .label--tall .spec { font-size: 18px; }
  .label--tall .mark { font-size: 9px; }
  .label--tall .mark-dot { width: 8px; height: 8px; }
  .label--tall .maker { font-size: 8.5px; }
  .label--tall .lot { font-size: 7.5px; }

  .label--wide .facts { left: 18px; top: 214px; width: 258px; height: 120px; }
  .label--wide .abv-cell { left: 0; top: 0; width: 88px; height: 70px; }
  .label--wide .logo-cell { left: 88px; top: 0; width: 81px; height: 70px; }
  .label--wide .volume-cell { left: 169px; top: 0; width: 89px; height: 70px; }
  .label--wide .maker-cell { left: 0; top: 70px; width: 258px; height: 22px; }
  .label--wide .lot-cell { left: 0; top: 92px; width: 258px; height: 28px; }
  .label--wide .spec { font-size: 14px; }
  .label--wide .mark { font-size: 7.5px; }
  .label--wide .mark-dot { width: 7px; height: 7px; }
  .label--wide .maker { font-size: 8px; letter-spacing: 0.04em; }
  .label--wide .lot { font-size: 7.5px; }
</style>
</head>
<body>
<main class="sheet">

  <section class="label label--tall" aria-label="Etikett Hochformat">
    <p class="house-name">HALLMEIER</p>
    <span class="house-rule"></span>
    <p class="house-line">EDELBRÄNDE</p>
    <h1 class="variety">Williams</h1>
    <span class="ornament ornament--left" role="img" aria-label="Rotes Zierornament"></span>
    <p class="product">BIRNEN<br>BRAND</p>
    <span class="ornament ornament--right" role="img" aria-label="Rotes Zierornament"></span>
    <div class="facts">
      <div class="cell logo-cell"><span class="mark"><span class="mark-dot"></span>Hallmeier</span></div>
      <div class="cell volume-cell"><span class="spec">500 ML<span class="estimated">℮</span></span></div>
      <div class="cell abv-cell"><span class="spec">40% VOL.</span></div>
      <div class="cell maker-cell"><p class="maker">Hallmeier Edelbrände<br>Brunnenweg 14 · 79999 Tannau - Lindenhof</p></div>
      <div class="cell lot-cell"><p class="lot">Losnummer K3F57382</p></div>
    </div>
  </section>

  <section class="label label--wide" aria-label="Etikett Querformat">
    <p class="house-name">HALLMEIER</p>
    <span class="house-rule"></span>
    <p class="house-line">EDELBRÄNDE</p>
    <h2 class="variety">Williams</h2>
    <span class="ornament ornament--left" role="img" aria-label="Rotes Zierornament"></span>
    <p class="product">BIRNENBRAND</p>
    <span class="ornament ornament--right" role="img" aria-label="Rotes Zierornament"></span>
    <div class="facts">
      <div class="cell abv-cell"><span class="spec">40% VOL.</span></div>
      <div class="cell logo-cell"><span class="mark"><span class="mark-dot"></span>Hallmeier</span></div>
      <div class="cell volume-cell"><span class="spec">500 ML<span class="estimated">℮</span></span></div>
      <div class="cell maker-cell"><p class="maker">Hallmeier Edelbrände · Brunnenweg 14 · 79999 Tannau - Lindenhof</p></div>
      <div class="cell lot-cell"><p class="lot">Losnummer K3F57382</p></div>
    </div>
  </section>

</main>
</body>
</html>
```